Plakate für Haushaltsnahe Dienstleistungen sowie Alltagsbegleitung
Zielgruppe
Wir sind eine Firma die Haushaltsnahe Dienstleistungen sowie Alltagsbegleitung anbietet. Unser Hauptkundenklientel sind Pflegebedürftige Menschen denen Haushaltshilfe von der Pflegekasse zu steht.
Aufgabenstellung
Es soll ein Roll-Up werden. Es soll drauf stehen: Abrechnung mit allen Pflegekasse möglich über den Entlastungsbetrag (ab Pflegegrad 1 bis 5) sowie Verhinderungspflege. Kontaktdaten sowie unsere Vorteile sollen auch drauf stehen.

```html
<!DOCTYPE html>
<html lang="de">
<head>
<meta charset="utf-8">
<title>Roll-Up – Wohlhafen Haushaltshilfen</title>
<link rel="stylesheet" href="https://fonts.googleapis.com/css2?family=Cinzel:wght@500;600;700&family=Poppins:wght@600;700&display=swap">
<style>
  :root {
    --brand-red: #c0182b;
    --brand-red-dark: #9e0c1c;
    --ink: #2b2b2b;
    --paper: #f7f6f6;
    --backdrop: #ebe9e7;
    --photo-beige: #d9c2ad;
    --photo-sand: #c7a78c;
    --photo-sofa: #8c7d82;
    --photo-wall: #e4ddd7;
    --photo-denim: #8ea3bd;
  }
  * { margin: 0; padding: 0; box-sizing: border-box; }
  html, body { width: 1200px; height: 1117px; overflow: hidden; background: var(--backdrop); }
  .rollup {
    position: absolute; left: 388px; top: 18px;
    width: 424px; height: 1080px;
    background: var(--paper);
    overflow: hidden;
    box-shadow: 0 6px 24px rgba(0,0,0,.12);
  }
  .rollup__top-band { position: absolute; left: 0; top: 0; width: 100%; height: 10px; background: var(--brand-red); }
  .rollup__wings { position: absolute; left: 0; top: 120px; width: 424px; height: 110px; }
  .brand-mark {
    position: absolute; left: 147px; top: 66px; width: 136px; height: 136px;
    border: 7px solid var(--brand-red); border-radius: 50%;
  }
  .brand {
    position: absolute; left: 0; top: 214px; width: 100%;
    text-align: center;
  }
  .brand__name {
    font-family: "Cinzel", serif; font-weight: 700;
    font-size: 37px; letter-spacing: 1px; color: var(--ink); line-height: 1;
  }
  .brand__tagline {
    font-family: "Cinzel", serif; font-weight: 600;
    font-size: 14px; color: var(--brand-red); letter-spacing: .5px; margin-top: 5px;
  }
  .headline {
    position: absolute; left: 0; top: 316px; width: 100%;
    text-align: center;
    font-family: "Cinzel", serif; font-weight: 600;
    font-size: 43px; line-height: 45px; color: var(--brand-red);
  }
  .subline {
    position: absolute; left: 0; top: 466px; width: 100%;
    text-align: center;
    font-family: "Cinzel", serif; font-weight: 600;
    font-size: 18px; line-height: 21px; color: var(--ink); letter-spacing: .3px;
  }
  .care-level {
    position: absolute; left: 77px; top: 547px; width: 277px; height: 38px;
    border-radius: 19px; background: var(--brand-red);
    box-shadow: 0 4px 0 #d6d4d4;
    font-family: "Poppins", sans-serif; font-weight: 700;
    font-size: 20px; color: #fff; line-height: 38px; text-align: center;
  }
  .photo {
    position: absolute; left: 0; top: 612px; width: 100%; height: 340px;
    background:
      linear-gradient(180deg, var(--paper) 0%, rgba(247,246,246,0) 22%),
      linear-gradient(90deg, var(--photo-beige) 0%, var(--photo-sand) 28%, var(--photo-sofa) 50%, var(--photo-wall) 62%, var(--photo-sand) 80%, var(--photo-beige) 100%);
  }
  .contact-band { position: absolute; left: 0; top: 880px; width: 424px; height: 200px; }
  .contact {
    position: absolute; left: 0; top: 0; width: 100%; height: 100%;
    font-family: "Poppins", sans-serif; font-weight: 600; color: #fff;
  }
  .contact__phone {
    position: absolute; left: 42px; top: 54px;
    display: flex; align-items: center; gap: 8px;
    font-size: 38px; font-weight: 700; line-height: 1;
  }
  .contact__line {
    position: absolute; display: flex; align-items: center; gap: 10px; font-size: 15px;
  }
  .contact__line--address { left: 52px; top: 108px; }
  .contact__line--email { left: 52px; top: 138px; }
  .contact__line--web { left: 238px; top: 130px; }
  .contact__icon { width: 13px; height: 13px; flex: none; }
</style>
</head>
<body>
  <div class="rollup">
    <div class="rollup__top-band"></div>

    <svg class="rollup__wings" viewBox="0 0 424 110" aria-hidden="true">
      <path d="M0 13 Q55 45 111 57 Q50 60 0 94 Z" fill="var(--brand-red)"/>
      <path d="M424 50 Q372 66 317 70 Q378 76 424 105 Z" fill="var(--brand-red)"/>
    </svg>

    <div class="brand-mark" aria-hidden="true"></div>

    <div class="brand">
      <div class="brand__name">WOHLHAFEN</div>
      <div class="brand__tagline">HAUSHALTSHILFEN &amp; MEHR</div>
    </div>

    <h1 class="headline">ABRECHNUNG<br>MIT ALLEN<br>PFLEGEKASSE</h1>

    <p class="subline">MÖGLICH ÜBER DEN<br>ENTLASTUNGSBETRAG SOWIE<br>VERHINDERUNGSPFLEGE</p>

    <div class="care-level">Ab Pflegegrad 1 bis 5</div>

    <div class="photo" role="img" aria-label="Foto: junge Frau und ältere Dame im Gespräch auf einem Sofa"></div>

    <div class="contact-band">
      <svg width="424" height="200" viewBox="0 0 424 200" aria-hidden="true" style="position:absolute;left:0;top:0">
        <defs>
          <linearGradient id="contactRed" x1="0" y1="0" x2="1" y2="1">
            <stop offset="0" stop-color="var(--brand-red)"/>
            <stop offset="1" stop-color="var(--brand-red-dark)"/>
          </linearGradient>
        </defs>
        <path d="M0 67 Q180 0 424 30 L424 200 L0 200 Z" fill="url(#contactRed)"/>
      </svg>

      <div class="contact">
        <div class="contact__phone">
          <svg width="32" height="32" viewBox="0 0 24 24" aria-hidden="true"><path fill="#fff" d="M6.6 10.8a15.1 15.1 0 0 0 6.6 6.6l2.2-2.2c.3-.3.7-.4 1-.2 1.1.4 2.3.6 3.6.6.6 0 1 .4 1 1V20c0 .6-.4 1-1 1C10.6 21 3 13.4 3 4c0-.6.4-1 1-1h3.5c.6 0 1 .4 1 1 0 1.3.2 2.5.6 3.6.1.3 0 .7-.2 1z"/></svg>
          <span>0711 20 30 4050</span>
        </div>
        <div class="contact__line contact__line--address">
          <svg class="contact__icon" viewBox="0 0 24 24" aria-hidden="true"><path fill="#fff" d="M12 2a7 7 0 0 0-7 7c0 5.2 7 13 7 13s7-7.8 7-13a7 7 0 0 0-7-7zm0 9.5A2.5 2.5 0 1 1 12 6.5a2.5 2.5 0 0 1 0 5z"/></svg>
          <span>Lindenweg 14, 70000 Musterstadt</span>
        </div>
        <div class="contact__line contact__line--email">
          <svg class="contact__icon" viewBox="0 0 24 24" aria-hidden="true"><circle cx="12" cy="12" r="11" fill="#fff"/><path d="M6.5 8.5h11v7h-11z M6.5 8.5l5.5 4 5.5-4" fill="none" stroke="var(--brand-red)" stroke-width="1.6"/></svg>
          <span>info@wohlhafen.de</span>
        </div>
        <div class="contact__line contact__line--web">
          <svg class="contact__icon" viewBox="0 0 24 24" aria-hidden="true"><circle cx="12" cy="12" r="11" fill="#fff"/><g fill="none" stroke="var(--brand-red)" stroke-width="1.5"><circle cx="12" cy="12" r="6"/><path d="M6 12h12M12 6c-3 3.5-3 8.5 0 12M12 6c3 3.5 3 8.5 0 12"/></g></svg>
          <span>www.wohlhafen.de</span>
        </div>
      </div>
    </div>
  </div>
</body>
</html>
```